Business Card Design Project

I would like to redesign our business cards and change the look and feel of our marketing material, but maintain the same basic identity of our current logo.
It is my belief that it could be much better.
You can view our website at kbozt.com

   

I was looking for a completely different look.  Something much more hip and cool looking.  You can change the colors.

I like this look and feel

 http://www.omdlawfirm.com

 But obviously don’t want to copy them exactly.

 

For the back just leave the last point.

“Focus on Your Business, and We’ll Focus on Your Claim”

I want there to be space for someone to write on.

                                                                    

                                       

I like this look and feel

 http://www.omdlawfirm.com

```html
<!DOCTYPE html>
<html lang="en">
<head>
<meta charset="utf-8">
<title>Harborline Recovery Professionals – Business Cards</title>
<link rel="stylesheet" href="https://fonts.googleapis.com/css2?family=Michroma&family=Saira:wght@400;500;600;700&display=swap">
<style>
  :root {
    --navy: #263f8e;
    --orange: #f59c1a;
    --paper: #f2f2f3;
    --white: #ffffff;
    --line-soft: rgba(255,255,255,0.35);
    --backdrop: #2b2b2d;
  }
  * { box-sizing: border-box; margin: 0; padding: 0; }
  html, body { width: 1200px; height: 900px; overflow: hidden; }
  body {
    background: var(--backdrop);
    font-family: "Saira", "Arial", sans-serif;
    position: relative;
  }
  .card {
    position: absolute;
    width: 540px;
    height: 309px;
    overflow: hidden;
    box-shadow: 0 10px 30px rgba(0,0,0,0.45);
  }

  /* Back of card */
  .card-back { left: 70px; top: 120px; background: var(--navy); }
  .card-back .rule {
    position: absolute; left: 0; right: 0; height: 1px; background: var(--white); opacity: 0.8;
  }
  .card-back .rule-top { top: 22px; }
  .card-back .rule-bottom { top: 146px; }
  .guide-band {
    position: absolute; left: 0; right: 0; top: 34px; height: 100px;
    background: var(--paper);
    border-top: 7px solid var(--orange);
    border-bottom: 7px solid var(--orange);
    display: flex; align-items: center; justify-content: center;
  }
  .guide-title {
    font-family: "Michroma", "Arial", sans-serif;
    font-size: 27px; font-weight: 400; letter-spacing: 0.5px; white-space: nowrap;
    color: var(--navy); -webkit-text-stroke: 0.8px var(--navy);
  }
  .guide-title .accent { color: var(--orange); -webkit-text-stroke: 0.8px var(--orange); }
  .promise {
    position: absolute; left: 40px; right: 30px; top: 162px;
    color: var(--white); font-size: 16px; line-height: 24px; white-space: nowrap;
  }
  .promise::before {
    content: ""; display: inline-block; width: 6px; height: 6px; border-radius: 50%;
    background: var(--orange); margin-right: 10px; vertical-align: middle;
  }
  .promise .accent { color: var(--orange); }
  .note-lines {
    position: absolute; left: 40px; right: 40px; top: 222px;
  }
  .note-lines span {
    display: block; height: 1px; background: var(--line-soft); margin-bottom: 30px;
  }

  /* Front of card */
  .card-front { left: 590px; top: 470px; background: var(--paper); }
  .front-lower {
    position: absolute; left: 0; right: 0; top: 158px; bottom: 0;
    background: var(--navy);
    border-top: 10px solid var(--orange);
  }
  .front-lower::before {
    content: ""; position: absolute; left: 0; right: 0; top: 5px; height: 1px;
    background: var(--white); opacity: 0.85;
  }
  .brand {
    position: absolute; left: 38px; top: 44px;
    display: flex; align-items: center; gap: 18px;
  }
  .brand-dot {
    width: 66px; height: 66px; border-radius: 50%; background: var(--orange);
  }
  .brand-name {
    font-weight: 700; font-size: 21px; line-height: 21px;
    color: var(--navy); text-transform: uppercase; letter-spacing: 0.3px;
  }
  .holder {
    position: absolute; left: 36px; top: 188px; color: var(--white);
  }
  .holder-name {
    color: var(--orange); font-size: 24px; font-weight: 400; letter-spacing: 1px;
    text-transform: uppercase; margin-bottom: 12px; white-space: nowrap;
  }
  .holder-address { font-size: 18px; line-height: 22px; letter-spacing: 0.5px; }
  .contact {
    position: absolute; right: 30px; top: 180px;
    color: var(--white); font-size: 15px; line-height: 20px; letter-spacing: 0.4px;
  }
  .contact dt { display: inline; color: var(--orange); }
  .contact dd { display: inline; }
  .contact dd::after { content: ""; display: block; }
  .contact .web { font-size: 19px; margin-top: 4px; letter-spacing: 0.8px; }
</style>
</head>
<body>

<section class="card card-back" aria-label="Card back">
  <div class="rule rule-top"></div>
  <div class="guide-band">
    <h2 class="guide-title">WE WILL BE <span class="accent">YOUR GUIDE</span></h2>
  </div>
  <div class="rule rule-bottom"></div>
  <p class="promise">Focus on Your Business, and <span class="accent">WE'LL FOCUS</span> on Your Claim</p>
  <div class="note-lines" aria-label="Space for handwritten notes">
    <span></span><span></span><span></span>
  </div>
</section>

<section class="card card-front" aria-label="Card front">
  <div class="brand">
    <span class="brand-dot"></span>
    <span class="brand-name">Harborline Recovery<br>Professionals</span>
  </div>
  <div class="front-lower"></div>
  <div class="holder">
    <p class="holder-name">Daniel Whitcombe</p>
    <p class="holder-address">214 Linden Avenue<br>Westbury, NY 11590</p>
  </div>
  <dl class="contact">
    <dt>Office:</dt> <dd>516.555.0142</dd>
    <dt>Cell:</dt> <dd>917.555.0187</dd>
    <dt>Email:</dt> <dd>dw@kbozt.com</dd>
    <dd class="web">www.kbozt.com</dd>
  </dl>
</section>

</body>
</html>
```